The first and only organic certified snacks manufacturer in Singapore (Brightmeadow Foods)needs a pac

We are a Singapore based certified organic snacks manufacturer and raw foods importing company. We deal with a variety of organic products and have been in the Singapore’s food industry for some time now. We are looking for a new packaging design for our product line TALORAN- Plain.
Design requirements:
1.We want a 10x10 cm label design that can be printed at the front and back of a stand-up pouch.
2. We need a design for around 15 different products that are uniform and can be extended easily to cover 30-40 products in future.
3. The stand-up pouch that we will be using is transparent, two sizes (12 x 6 x 21 cm and 16 x 8 x 23 cm), and the label is 10x10 cm
4. We don't have a brand logo and are currently using the word Taloran as the logo, the font is Glacial Indifference.
5.We need a design that is contemporary, clean and simple and using different colour combinations except green and brown(overused by organic competitors)
6.One label/print on each front and back, ca 10x10 cm.
Essential information:
Contents:
1.Filling weight
2.Product nameï‚§
3.Brand name and/or logo (yet to be designed)
4.Originï‚§
5.EU/USDA/HALAL logosï‚§
6.BMF (brightmeadow foods) logo
7.Expiration date

7.The original file should be in the .ai (Adobe Illustrator) format.
Please find attached the certification logos, fonts and the current TALORAN-Plain .ai files

Target Market(s)

everyone who likes to eat and use healthy products

Industry/Entity Type

Food Production

Font styles to use
Other font styles liked:
• Glacial Indiffrence

Colors
fbf063
00a990
85cae6
3377b5
876aae
b768aa
e667a6
f04a50
ffc214

Requirements
Must have
• contemporary clean designs. use of different patterns is suggested
Nice to have
Should not have
• too much use of green, orange and brown colour. pictures of food products.

```html
<!DOCTYPE html>
<html lang="en">
<head>
<meta charset="utf-8">
<title>Taloran Plain – Label Range</title>
<link rel="stylesheet" href="https://fonts.googleapis.com/css2?family=League+Spartan:wght@700&family=Questrial&display=swap">
<style>
  :root {
    --ink: #111111;
    --page: #ffffff;
    --apricot-ground: #d6e59b;
    --apricot-panel: #f8d3e5;
    --hazelnut-ground: #a9dde6;
    --hazelnut-panel: #f9d4dc;
    --mulberry-ground: #f6b9a2;
    --mulberry-panel: #c8e6f4;
    --fig-ground: #fde39c;
    --fig-panel: #e2d1e4;
  }
  * { box-sizing: border-box; margin: 0; padding: 0; }
  html, body {
    width: 1200px;
    height: 1189px;
    overflow: hidden;
    background: var(--page);
  }
  .label-range {
    position: relative;
    width: 1200px;
    height: 1189px;
  }
  .label {
    position: absolute;
    width: 523px;
    height: 523px;
  }
  .label--apricots { left: 50px; top: 50px; }
  .label--hazelnuts { left: 628px; top: 50px; }
  .label--mulberries { left: 50px; top: 624px; }
  .label--figs { left: 628px; top: 624px; }

  .label__ground {
    position: absolute;
    inset: 0;
  }
  .label--apricots .label__ground { background: var(--apricot-ground); }
  .label--hazelnuts .label__ground { background: var(--hazelnut-ground); }
  .label--mulberries .label__ground { background: var(--mulberry-ground); }
  .label--figs .label__ground { background: var(--fig-ground); }

  .label__panel {
    position: absolute;
    left: 70px;
    top: 78px;
    width: 380px;
    height: 362px;
    border: 6px solid var(--ink);
    padding: 46px 36px 0 38px;
    color: var(--ink);
  }
  .label--apricots .label__panel { background: var(--apricot-panel); }
  .label--hazelnuts .label__panel { background: var(--hazelnut-panel); }
  .label--mulberries .label__panel { background: var(--mulberry-panel); }
  .label--figs .label__panel { background: var(--fig-panel); }

  .brand {
    font-family: "League Spartan", "Arial Black", sans-serif;
    font-weight: 700;
    font-size: 42px;
    line-height: 42px;
    letter-spacing: 0.5px;
  }
  .zigzag {
    display: block;
    width: 296px;
    height: 12px;
    margin-top: 10px;
  }
  .product__kind {
    font-family: "Questrial", sans-serif;
    font-size: 28px;
    line-height: 30px;
    margin-top: 14px;
  }
  .product__name {
    font-family: "Questrial", sans-serif;
    font-size: 42px;
    line-height: 44px;
    letter-spacing: 0.5px;
  }
  .product__name + .zigzag { margin-top: 6px; }

  .label__footer {
    position: absolute;
    left: 38px;
    right: 26px;
    bottom: 22px;
    display: flex;
    align-items: center;
  }
  .cert-badges { display: flex; gap: 5px; }
  .cert-badge {
    width: 20px;
    height: 20px;
    border: 2px solid var(--ink);
    border-radius: 50%;
  }
  .cert-badge--square { border-radius: 3px; }
  .maker {
    margin-left: 10px;
    font-family: "Questrial", sans-serif;
    color: var(--ink);
    line-height: 1;
  }
  .maker__note { font-size: 6px; display: block; margin-left: 22px; }
  .maker__name {
    display: flex;
    align-items: center;
    gap: 4px;
    font-size: 12px;
    margin-top: 1px;
  }
  .maker__dot {
    width: 18px;
    height: 18px;
    border-radius: 50%;
    background: var(--ink);
  }
  .net-weight {
    margin-left: auto;
    font-family: "Questrial", sans-serif;
    font-size: 13px;
  }
</style>
</head>
<body>
<svg width="0" height="0" style="position:absolute" aria-hidden="true">
  <defs>
    <pattern id="zigzag-line" width="12" height="12" patternUnits="userSpaceOnUse">
      <path d="M0 10 L6 2 L12 10" fill="none" stroke="#111111" stroke-width="2.2"/>
    </pattern>
  </defs>
</svg>

<main class="label-range">

  <section class="label label--apricots">
    <div class="label__ground" role="img" aria-label="White bubble pattern on soft lime green"></div>
    <div class="label__panel">
      <h2 class="brand">TALORAN<br>PLAIN</h2>
      <svg class="zigzag" viewBox="0 0 296 12" aria-hidden="true"><rect width="296" height="12" fill="url(#zigzag-line)"/></svg>
      <p class="product__kind">ORGANIC SUN-DRIED</p>
      <p class="product__name">APRICOTS</p>
      <svg class="zigzag" viewBox="0 0 296 12" aria-hidden="true"><rect width="296" height="12" fill="url(#zigzag-line)"/></svg>
      <div class="label__footer">
        <div class="cert-badges"><span class="cert-badge"></span><span class="cert-badge cert-badge--square"></span><span class="cert-badge cert-badge--square"></span><span class="cert-badge"></span></div>
        <div class="maker"><span class="maker__note">packed by</span><span class="maker__name"><span class="maker__dot"></span>Brightmeadow Foods</span></div>
        <span class="net-weight">250 G ℮</span>
      </div>
    </div>
  </section>

  <section class="label label--hazelnuts">
    <div class="label__ground" role="img" aria-label="White dotted pattern on light aqua blue"></div>
    <div class="label__panel">
      <h2 class="brand">TALORAN<br>PLAIN</h2>
      <svg class="zigzag" viewBox="0 0 296 12" aria-hidden="true"><rect width="296" height="12" fill="url(#zigzag-line)"/></svg>
      <p class="product__kind">ORGANIC ROASTED</p>
      <p class="product__name">HAZELNUTS</p>
      <svg class="zigzag" viewBox="0 0 296 12" aria-hidden="true"><rect width="296" height="12" fill="url(#zigzag-line)"/></svg>
      <div class="label__footer">
        <div class="cert-badges"><span class="cert-badge"></span><span class="cert-badge cert-badge--square"></span><span class="cert-badge cert-badge--square"></span><span class="cert-badge"></span></div>
        <div class="maker"><span class="maker__note">packed by</span><span class="maker__name"><span class="maker__dot"></span>Brightmeadow Foods</span></div>
        <span class="net-weight">250 G ℮</span>
      </div>
    </div>
  </section>

  <section class="label label--mulberries">
    <div class="label__ground" role="img" aria-label="White arc pattern on soft coral peach"></div>
    <div class="label__panel">
      <h2 class="brand">TALORAN<br>PLAIN</h2>
      <svg class="zigzag" viewBox="0 0 296 12" aria-hidden="true"><rect width="296" height="12" fill="url(#zigzag-line)"/></svg>
      <p class="product__kind">ORGANIC SUN-DRIED</p>
      <p class="product__name">MULLBERRIES</p>
      <svg class="zigzag" viewBox="0 0 296 12" aria-hidden="true"><rect width="296" height="12" fill="url(#zigzag-line)"/></svg>
      <div class="label__footer">
        <div class="cert-badges"><span class="cert-badge"></span><span class="cert-badge cert-badge--square"></span><span class="cert-badge cert-badge--square"></span><span class="cert-badge"></span></div>
        <div class="maker"><span class="maker__note">packed by</span><span class="maker__name"><span class="maker__dot"></span>Brightmeadow Foods</span></div>
        <span class="net-weight">250 G ℮</span>
      </div>
    </div>
  </section>

  <section class="label label--figs">
    <div class="label__ground" role="img" aria-label="White diagonal dash pattern on pale sunny yellow"></div>
    <div class="label__panel">
      <h2 class="brand">TALORAN<br>PLAIN</h2>
      <svg class="zigzag" viewBox="0 0 296 12" aria-hidden="true"><rect width="296" height="12" fill="url(#zigzag-line)"/></svg>
      <p class="product__kind">ORGANIC SUN-DRIED</p>
      <p class="product__name">FIGS</p>
      <svg class="zigzag" viewBox="0 0 296 12" aria-hidden="true"><rect width="296" height="12" fill="url(#zigzag-line)"/></svg>
      <div class="label__footer">
        <div class="cert-badges"><span class="cert-badge"></span><span class="cert-badge cert-badge--square"></span><span class="cert-badge cert-badge--square"></span><span class="cert-badge"></span></div>
        <div class="maker"><span class="maker__note">packed by</span><span class="maker__name"><span class="maker__dot"></span>Brightmeadow Foods</span></div>
        <span class="net-weight">250 G ℮</span>
      </div>
    </div>
  </section>

</main>
</body>
</html>
```